New Bicycle shop business card

Hi!
I'm looking for a business card for my new proffesional bike mechanics shop. This shop is only for fixing broken bikes and not selling bikes.
Peferbly a modern and sleek and modern design.
Colors: black, grey, red, white
Information:
Name: Rijwielwerkplaats Vanhoutem
Shop owner: Bart Vanhoutem & Sanne Maertens
Website: www.rijwielwerkplaats-vanhoutem.be
Email: info@rijwielwerkplaats-vanhoutem.be
Phone number: +32471902386
Street adres: Kerkweg 64
9970 Oostmoere
Slogan/shop information: Herstellingen van alle merken.
Logo: see files.
Target Market(s)
People who seek a mechanic to fix or upgrade their bikes.
Contact Information for Business Card
Information:
Website: info@rijwielwerkplaats-vanhoutem.be
9970 Oostmoere
Logo: see files.

```html
<!DOCTYPE html>
<html lang="nl">
<head>
<meta charset="utf-8">
<title>Rijwielwerkplaats Vanhoutem – visitekaartje</title>
<link rel="stylesheet" href="https://fonts.googleapis.com/css2?family=Fira+Sans:wght@400;700&display=swap">
<style>
  :root {
    --brand-red: #d92838;
    --ink-black: #141414;
    --paper-white: #ffffff;
    --steel-grey: #9a9a9a;
    --backdrop: #e7ebeb;
  }
  * { box-sizing: border-box; margin: 0; padding: 0; }
  html, body {
    width: 1200px;
    height: 900px;
    overflow: hidden;
    background: var(--backdrop);
    font-family: "Fira Sans", Arial, sans-serif;
  }
  .sheet {
    width: 1200px;
    height: 900px;
    display: flex;
    align-items: center;
    justify-content: center;
    gap: 80px;
  }
  .card {
    background: var(--brand-red);
    color: var(--paper-white);
    box-shadow: 0 10px 28px rgba(0,0,0,0.14);
  }

  /* Front */
  .card-front {
    width: 560px;
    height: 362px;
    display: flex;
    align-items: center;
    justify-content: center;
  }
  .wordmark {
    display: flex;
    align-items: center;
    gap: 14px;
  }
  .wordmark-dot {
    width: 18px;
    height: 18px;
    border-radius: 50%;
    background: var(--ink-black);
  }
  .wordmark-name {
    font-weight: 700;
    font-size: 28px;
    letter-spacing: 0.5px;
    color: var(--ink-black);
  }

  /* Back */
  .card-back {
    width: 362px;
    height: 560px;
    display: flex;
    flex-direction: column;
  }
  .back-band {
    height: 150px;
    background: var(--paper-white);
    display: flex;
    align-items: center;
    justify-content: center;
    gap: 10px;
  }
  .back-band .wordmark-dot { background: var(--brand-red); width: 14px; height: 14px; }
  .back-band .wordmark-name { color: var(--brand-red); font-size: 19px; }
  .back-body {
    flex: 1;
    padding: 34px 32px 30px 32px;
    display: flex;
    flex-direction: column;
    align-items: flex-end;
    text-align: right;
  }
  .shop-name {
    font-weight: 700;
    font-size: 19px;
    line-height: 1.2;
  }
  .owners {
    font-size: 13px;
    margin-top: 4px;
  }
  .address {
    font-size: 13px;
    line-height: 1.45;
    margin-top: 20px;
  }
  .contact-icons {
    display: flex;
    gap: 8px;
    margin-top: 14px;
  }
  .contact-icons svg { width: 13px; height: 13px; display: block; }
  .contact-list {
    list-style: none;
    font-size: 13px;
    line-height: 1.5;
    margin-top: 8px;
  }
  .divider {
    width: 150px;
    height: 1.5px;
    background: var(--paper-white);
    margin-top: 26px;
    align-self: flex-start;
  }
  .slogan {
    font-size: 13px;
    margin-top: auto;
    align-self: flex-start;
  }
</style>
</head>
<body>
<main class="sheet">

  <section class="card card-front" aria-label="Voorkant visitekaartje">
    <div class="wordmark">
      <span class="wordmark-dot"></span>
      <span class="wordmark-name">Rijwielwerkplaats Vanhoutem</span>
    </div>
  </section>

  <section class="card card-back" aria-label="Achterkant visitekaartje">
    <div class="back-band">
      <span class="wordmark-dot"></span>
      <span class="wordmark-name">Rijwielwerkplaats Vanhoutem</span>
    </div>
    <div class="back-body">
      <h1 class="shop-name">Rijwielwerkplaats Vanhoutem</h1>
      <p class="owners">Owner: Bart Vanhoutem &amp; Sanne Maertens</p>
      <p class="address">Kerkweg 64<br>9970 Oostmoere</p>
      <div class="contact-icons" aria-hidden="true">
        <svg viewBox="0 0 16 16"><path fill="#fff" d="M3.5 1.5l2.5 0 1 3.5-1.6 1.2c.8 1.8 2.2 3.2 4 4l1.2-1.6 3.5 1v2.5c0 .8-.7 1.5-1.5 1.5C7 13.6 2.4 9 2 3c0-.8.7-1.5 1.5-1.5z"/></svg>
        <svg viewBox="0 0 16 16"><rect x="1" y="3" width="14" height="10" rx="1" fill="#fff"/><path d="M1.5 3.5L8 9l6.5-5.5" stroke="#d92838" stroke-width="1.4" fill="none"/></svg>
        <svg viewBox="0 0 16 16"><circle cx="8" cy="8" r="6.5" fill="#fff"/><path d="M1.5 8h13M8 1.5c-2.2 2-2.2 11 0 13M8 1.5c2.2 2 2.2 11 0 13" stroke="#d92838" stroke-width="1.1" fill="none"/></svg>
      </div>
      <ul class="contact-list">
        <li>+32471902386</li>
        <li>info@rijwielwerkplaats-vanhoutem.be</li>
        <li>www.rijwielwerkplaats-vanhoutem.be</li>
      </ul>
      <span class="divider"></span>
      <p class="slogan">Herstellingen van alle merken.</p>
    </div>
  </section>

</main>
</body>
</html>
```